Brantley Water Taxi and Transport

Need to redesign our business cards to relay that we do freight logistics and water taxi service. We also work with gov. agencies doing environmental clean up, oil spill response, remote site construction and work with many of the air taxi and helicopter services on Kodiak Island. Out website is www.brantleywatertaxi-example.com to get a better idea of what we do.

Contact Information for Business Card

I have a previous business card but it just has the logo on the front, and a sunset picture on the back with the contact info. It does not relay what we do and what we can help with. I like a simple straight forward design over a busy one.

Colors
3176b5
0455a3
cfdfed

Requirements
Must have
• logo, email, website, phone number

```html
<!DOCTYPE html>
<html lang="en">
<head>
<meta charset="utf-8">
<title>Brantley Water Taxi &amp; Transport – Business Card</title>
<link href="https://fonts.googleapis.com/css2?family=Poppins:wght@400;500;600&display=swap" rel="stylesheet">
<style>
  :root {
    --navy: #0a3f8f;
    --blue: #0455a3;
    --sky: #3176b5;
    --mist: #cfdfed;
    --orange: #f0961e;
    --white: #ffffff;
    --backdrop: #e6e9ee;
  }
  * { box-sizing: border-box; margin: 0; padding: 0; }
  html, body {
    width: 1200px; height: 900px; overflow: hidden;
    background: var(--backdrop);
    font-family: "Poppins", sans-serif;
  }
  .sheet {
    width: 1200px; height: 900px;
    display: flex; flex-direction: column;
    align-items: center; justify-content: center; gap: 56px;
  }
  .card {
    position: relative;
    width: 560px; height: 320px;
    border-radius: 4px;
    overflow: hidden;
    background: linear-gradient(135deg, var(--blue), var(--navy));
    box-shadow: 0 12px 30px rgba(10, 30, 70, 0.25);
  }
  .card-shape { position: absolute; inset: 0; width: 100%; height: 100%; }

  /* front */
  .contact {
    position: absolute; left: 28px; top: 44px;
    color: var(--white);
    font-size: 12px; line-height: 1.6;
    white-space: nowrap;
  }
  .contact-name {
    color: var(--orange);
    font-size: 22px; font-weight: 500;
    letter-spacing: 0.5px; text-transform: uppercase;
    line-height: 1.2;
  }
  .contact-role { font-size: 14px; margin-bottom: 12px; }
  .contact-address { margin-bottom: 8px; }
  .contact-line { display: flex; align-items: center; gap: 8px; }
  .contact-icon { width: 11px; height: 11px; flex: none; }

  .brand {
    position: absolute;
    display: flex; align-items: center; gap: 10px;
    font-weight: 600;
  }
  .brand-dot { width: 16px; height: 16px; border-radius: 50%; background: var(--orange); flex: none; }
  .brand-name { line-height: 1.1; }
  .brand-name .brand-main { display: block; font-size: 32px; letter-spacing: 1px; text-transform: uppercase; }
  .brand-name .brand-sub { display: block; font-size: 13px; }

  .card-front .brand { right: 28px; top: 136px; color: var(--blue); }
  .card-back .brand { left: 50%; top: 50%; transform: translate(-50%, -50%); color: var(--white); }
  .card-back .brand-dot { width: 18px; height: 18px; }
  .card-back .brand-name .brand-main { font-size: 46px; }
  .card-back .brand-name .brand-sub { font-size: 18px; }
</style>
</head>
<body>
<main class="sheet">

  <section class="card card-front" aria-label="Business card front">
    <svg class="card-shape" viewBox="0 0 560 320" preserveAspectRatio="none" aria-hidden="true">
      <path d="M312 0 Q232 170 392 320" fill="none" stroke="var(--white)" stroke-width="10"/>
      <path d="M319 0 Q240 170 399 320" fill="none" stroke="var(--orange)" stroke-width="7"/>
      <path d="M330 0 Q252 170 410 320 L560 320 L560 0 Z" fill="var(--white)"/>
    </svg>

    <div class="contact">
      <p class="contact-name">Dorian Hale</p>
      <p class="contact-role">Director</p>
      <p class="contact-address">415 Harbor View Road<br>Port Lindell, AK 99615</p>
      <p class="contact-line">
        <svg class="contact-icon" viewBox="0 0 24 24" aria-hidden="true"><path fill="var(--orange)" d="M6.6 10.8a15 15 0 0 0 6.6 6.6l2.2-2.2a1 1 0 0 1 1-.25 11.4 11.4 0 0 0 3.6.57 1 1 0 0 1 1 1V20a1 1 0 0 1-1 1A17 17 0 0 1 3 4a1 1 0 0 1 1-1h3.5a1 1 0 0 1 1 1c0 1.25.2 2.45.57 3.57a1 1 0 0 1-.25 1z"/></svg>
        907-555-0148
      </p>
      <p class="contact-line">
        <svg class="contact-icon" viewBox="0 0 24 24" aria-hidden="true"><rect x="2" y="5" width="20" height="14" rx="2" fill="none" stroke="var(--orange)" stroke-width="2"/><path d="M3 6l9 7 9-7" fill="none" stroke="var(--orange)" stroke-width="2"/></svg>
        brantleywatertaxi@example-mail.com
      </p>
      <p class="contact-line">
        <svg class="contact-icon" viewBox="0 0 24 24" aria-hidden="true"><circle cx="12" cy="12" r="9.5" fill="none" stroke="var(--orange)" stroke-width="2"/><path d="M2.5 12h19M12 2.5c3 3 3 16 0 19M12 2.5c-3 3-3 16 0 19" fill="none" stroke="var(--orange)" stroke-width="1.6"/></svg>
        www.brantleywatertaxi-example.com
      </p>
    </div>

    <div class="brand">
      <span class="brand-dot" aria-hidden="true"></span>
      <p class="brand-name"><span class="brand-main">Brantley</span><span class="brand-sub">Water Taxi &amp; Transport</span></p>
    </div>
  </section>

  <section class="card card-back" aria-label="Business card back">
    <div class="brand">
      <span class="brand-dot" aria-hidden="true"></span>
      <p class="brand-name"><span class="brand-main">Brantley</span><span class="brand-sub">Water Taxi &amp; Transport</span></p>
    </div>
  </section>

</main>
</body>
</html>
```